New Website Design for PALVO.org

We are looking for a new website design for PALVO.org. PALVO is a non profit home inspector association based in California. Home Inspectors are people that come out and look at a house before it's purchased to let the buyer know of any defects that may exist.
Our site is based on Joomla so if you'll be able to make a Joomla 3 template as well, please let us know (not required, but a bonus).
We would like to see designs that incorporate royal blue, white and chrome into the site as that's our main business colors.
We would like a place for rotating banners though they don't need to be the same size as the current site.
We would like navigation to be easier to manage with menus only across the top (via drop down menus) where we are going to sort out the items currently on the side. Possibly the front page could have a graphic link to separate portals for Realtors, Home Buyers and Inspectors, but that's just one option.
We would like a good mobile design or something that will scale easily to mobile.
The Find an Inspector feature is important and should stand out. The ZIM PALVOr site
Current home page feels a bit busy. Would like to simplify a bit.

```html
<!DOCTYPE html>
<html lang="en">
<head>
<meta charset="utf-8">
<title>PALVO.org – Home</title>
<link rel="stylesheet" href="https://fonts.googleapis.com/css2?family=PT+Sans:wght@400;700&display=swap">
<style>
:root{
  --royal:#2b3f92;
  --royal-dark:#223378;
  --ink:#333333;
  --muted:#8a8a8a;
  --light:#f4f4f4;
  --band:#e6e6e6;
  --panel:#ffffff;
  --dark:#3b3b3b;
  --darker:#2a2a2a;
  --chrome:#5a5a5a;
  --line:#d6d6d6;
}
*{box-sizing:border-box;margin:0;padding:0}
html,body{width:1200px;height:2633px;overflow:hidden}
body{font-family:"PT Sans",Arial,sans-serif;color:var(--ink);background:var(--light);position:relative;font-size:13px}
.abs{position:absolute}
.topbar{left:0;top:0;width:1200px;height:53px;background:var(--royal);color:#fff;font-size:13px}
.topbar .item{top:18px;display:flex;align-items:center;gap:10px}
.topbar .login{right:0;top:0;width:180px;height:53px;background:#454545;font-weight:700;display:flex;align-items:center;justify-content:center;letter-spacing:1px}
.header{left:0;top:53px;width:1200px;height:127px;background:#fff}
.brand{left:182px;top:18px;display:flex;align-items:center;gap:14px}
.brand .mark{width:96px;height:96px;border-radius:50%;background:var(--royal);display:flex;align-items:center;justify-content:center;color:#fff;font-weight:700;font-size:22px}
.nav{left:392px;top:68px;display:flex;gap:34px;font-weight:700;font-size:16px;text-transform:uppercase;color:#2d2d2d}
.nav .active{color:var(--royal)}
.search{left:988px;top:62px;width:26px;height:26px;border:1px solid #bbb;border-radius:50%}
.hero{left:0;top:180px;width:1200px;height:408px;background:linear-gradient(120deg,#1f3b78 0%,#6f8fbf 30%,#d9e3ef 55%,#4a6aa0 80%,#1b2f5e 100%)}
.hero-card{left:610px;top:180px;width:410px;height:355px;background:rgba(40,40,40,.9);color:#fff;text-align:center;padding:60px 40px 0}
.hero-card h1{font-size:25px;line-height:36px;font-weight:700;letter-spacing:1px}
.hero-card p{font-size:16px;line-height:20px;margin-top:24px;color:#e6e6e6}
.hero-card .more{margin-top:42px;display:flex;justify-content:center;align-items:center;gap:16px;font-size:13px}
.dot{display:inline-flex;width:20px;height:20px;border-radius:50%;background:#fff;align-items:center;justify-content:center}
.dot.dark{background:#4a4a4a}
.features{left:0;top:588px;width:1200px;height:318px;background:#f2f2f2}
.feature{top:56px;width:300px;text-align:center}
.feature .icon{margin:0 auto;width:96px;height:96px;border-radius:50%;background:#dcdcdc;display:flex;align-items:center;justify-content:center}
.feature .icon span{width:78px;height:78px;border-radius:50%;background:var(--chrome);display:flex;align-items:center;justify-content:center}
.feature h3{margin-top:38px;color:var(--royal);font-size:18px;text-transform:uppercase}
.feature p{margin-top:12px;color:var(--muted);font-size:11px;line-height:15px}
.about{left:0;top:906px;width:1200px;height:801px;background:var(--band)}
.heading{color:var(--royal);font-weight:700;font-size:16px;text-transform:uppercase}
.photo{border:1px solid #fff}
.small{font-size:11px;line-height:15px;color:var(--muted)}
.callout{left:182px;top:1132px;width:836px;height:79px;background:#fff}
.callout .label{left:665px;top:0;width:171px;height:79px;background:#444;color:#fff;font-weight:700;font-size:16px;display:flex;align-items:center;justify-content:center}
.why-item{width:200px}
.why-item h4{color:var(--royal);font-size:13px;text-transform:uppercase;margin-left:34px}
.why-item p{margin-left:34px;margin-top:4px}
.why-item svg{position:absolute;left:0;top:0}
.info{left:0;top:1707px;width:1200px;height:344px;background:#f4f4f4}
.col-title{font-weight:700;font-size:13px;text-transform:uppercase;color:#2d2d2d}
.date{width:32px;height:44px;color:#fff;text-align:center;font-size:13px;font-weight:700;padding-top:6px}
.date small{display:block;font-size:8px;font-weight:400}
.news-row{display:flex;align-items:center;gap:14px;font-size:11px}
.sq{width:18px;height:18px;background:#ddd;color:#666;display:flex;align-items:center;justify-content:center;font-weight:700}
.quote{left:762px;top:1796px;width:256px;height:96px;background:#444;color:#eee;font-size:10px;line-height:13px;padding:16px 18px}
.partners{left:0;top:2051px;width:1200px;height:248px;background:#ededed}
.partner{top:2170px;color:#555;font-weight:700;font-size:32px;display:flex;align-items:center;gap:10px}
.footer{left:0;top:2299px;width:1200px;height:242px;background:var(--dark);color:#ddd}
.footer h5{color:#fff;font-size:14px;text-transform:uppercase}
.footer .txt{font-size:12px;line-height:16px;color:#ccc}
.thumb{width:72px;height:44px;background:linear-gradient(135deg,#6c7f9a,#c9cdd4)}
.tweet{width:236px;height:40px;background:#2c2c2c;display:flex;align-items:center;gap:10px;padding:0 10px;font-size:9px;color:#aaa}
.bottombar{left:0;top:2541px;width:1200px;height:92px;background:var(--darker);color:#bbb;font-size:12px}
</style>
</head>
<body>

<div class="abs topbar">
  <div class="abs item" style="left:182px"><svg width="14" height="14" viewBox="0 0 14 14"><path d="M3 1l3 3-2 2c1 2 2 3 4 4l2-2 3 3-2 2C5 12 2 9 1 3z" fill="#fff"/></svg>+800 555 0142 or 916 555 0187</div>
  <div class="abs item" style="left:460px"><svg width="16" height="12" viewBox="0 0 16 12"><rect width="16" height="12" rx="2" fill="#fff"/><path d="M1 1l7 6 7-6" stroke="#2b3f92" fill="none"/></svg>ceo@palvo.org</div>
  <div class="abs item" style="left:608px"><svg width="14" height="14" viewBox="0 0 14 14"><circle cx="7" cy="7" r="7" fill="#fff"/></svg>ask to PALVO</div>
  <div class="abs login">LOGIN</div>
</div>

<header class="abs header">
  <div class="abs brand"><div class="mark">PALVO</div></div>
  <nav class="abs nav">
    <span class="active">Home</span><span>About us</span><span>Products</span><span>Info</span><span>Applications</span><span>Contact us</span>
  </nav>
  <div class="abs search"><svg width="24" height="24" viewBox="0 0 24 24"><circle cx="11" cy="11" r="4" stroke="#777" fill="none" stroke-width="1.5"/><path d="M14 14l3 3" stroke="#777" stroke-width="1.5"/></svg></div>
</header>

<section class="abs hero" role="img" aria-label="Banner photo of a glass and steel building roof seen from below"></section>
<div class="abs hero-card">
  <h1>LOREM IPSUM DOLAR SIT<br>OMNIS EXPLICABO</h1>
  <p>aspernatur magni quae aperiam averitatis voluptas doloremque &nbsp;error natus natus, qui aut eaque inventore</p>
  <div class="more">amet rem eos <span class="dot"><svg width="8" height="8" viewBox="0 0 8 8"><path d="M2 1l4 3-4 3z" fill="#333"/></svg></span></div>
</div>

<section class="abs features">
  <div class="abs feature" style="left:172px">
    <div class="icon"><span><svg width="30" height="34" viewBox="0 0 30 34"><path d="M5 3h20v16l-10 12-10-12z" fill="#fff"/></svg></span></div>
    <h3>Inspector Finder</h3>
    <p>perspiciatis beatae magni architecto odit odit<br>aspernatur magni quae aperiam aut veritatis beatae<br>eos aut voluptas doloremque perspiciatis</p>
  </div>
  <div class="abs feature" style="left:447px">
    <div class="icon"><span><svg width="34" height="34" viewBox="0 0 34 34"><circle cx="17" cy="17" r="16" fill="#fff"/><rect x="8" y="11" width="18" height="12" fill="#5a5a5a"/><path d="M8 11l9 7 9-7" stroke="#fff" fill="none" stroke-width="1.5"/></svg></span></div>
    <h3>Tie Message Boards</h3>
    <p>perspiciatis beatae magni architecto odit odit<br>aspernatur magni quae aperiam aut veritatis beatae<br>eos aut voluptas doloremque perspiciatis</p>
  </div>
  <div class="abs feature" style="left:728px">
    <div class="icon"><span><svg width="34" height="34" viewBox="0 0 34 34"><path d="M4 17L17 4h12v12L16 29z" fill="#fff"/><circle cx="23" cy="10" r="2.5" fill="#5a5a5a"/></svg></span></div>
    <h3>PALVO Online Store</h3>
    <p>perspiciatis beatae magni architecto odit odit<br>aspernatur magni quae aperiam aut veritatis beatae<br>eos aut voluptas doloremque perspiciatis</p>
  </div>
</section>

<section class="abs about">
  <div class="abs heading" style="left:182px;top:26px">About us</div>
  <div class="abs photo" style="left:182px;top:62px;width:191px;height:103px;background:linear-gradient(135deg,#6a86a8,#d6dde6)" role="img" aria-label="Photo of people at a laptop with a video play button"></div>
  <div class="abs photo" style="left:386px;top:62px;width:189px;height:103px;background:linear-gradient(135deg,#7a8594,#dfe3e8)" role="img" aria-label="Photo of a man in a suit in an office"></div>
  <div class="abs photo" style="left:586px;top:62px;width:191px;height:103px;background:linear-gradient(135deg,#8d99a8,#eef0f3)" role="img" aria-label="Photo of a business team around a table"></div>
  <div class="abs" style="left:801px;top:60px;width:220px">
    <div class="col-title" style="font-size:12px;line-height:17px">Welcome to PALVO<br>consequuntur</div>
    <p class="small" style="margin-top:10px">Voluptatem doloremque persp beatae ratione ratione dolores unde</p>
    <div style="margin-top:12px;display:flex;align-items:center;gap:12px" class="small">learn more <span class="dot dark" style="width:18px;height:18px"><svg width="8" height="8" viewBox="0 0 8 8"><path d="M2 1l4 3-4 3z" fill="#fff"/></svg></span></div>
  </div>

  <div class="abs heading" style="left:182px;top:357px">Recent customers</div>
  <p class="abs small" style="left:182px;top:385px;width:200px">Dolores ut voluptatem doloremque perspi beatae quia ratione ratione dolores Unde quasi ratione inventore ipsa explicabo</p>
  <div class="abs small" style="left:182px;top:446px;display:flex;align-items:center;gap:12px">view more <span class="dot dark" style="width:18px;height:18px"><svg width="8" height="8" viewBox="0 0 8 8"><path d="M2 1l4 3-4 3z" fill="#fff"/></svg></span></div>
  <div class="abs" style="left:410px;top:362px;width:189px;height:121px;background:linear-gradient(135deg,#b9a596,#e9e4df)" role="img" aria-label="Photo of colleagues smiling at a meeting"></div>
  <div class="abs" style="left:614px;top:362px;width:196px;height:121px;background:linear-gradient(135deg,#8fa3b6,#e7ebef)" role="img" aria-label="Photo of a team shaking hands"></div>
  <div class="abs" style="left:823px;top:362px;width:195px;height:121px;background:linear-gradient(135deg,#a59485,#ede7e1)" role="img" aria-label="Photo of a group of coworkers"></div>
  <p class="abs small" style="left:410px;top:500px;width:189px;text-align:center">Nemo rem ipsam quas illo<br>dolores ut voluptatem explicabo</p>
  <p class="abs small" style="left:614px;top:500px;width:196px;text-align:center">Nemo rem ipsam quas illo<br>dolores ut voluptatem explicabo</p>
  <p class="abs small" style="left:823px;top:500px;width:195px;text-align:center">Nemo rem ipsam quas illo<br>dolores ut voluptatem explicabo</p>

  <div class="abs heading" style="left:0;width:1200px;text-align:center;top:576px">Why choose us</div>
  <div class="abs" style="left:182px;top:614px;width:836px;border-top:1px solid var(--line)"></div>
</section>

<div class="abs callout">
  <div class="abs" style="left:34px;top:20px;color:var(--royal);font-weight:700;font-size:12px">SED ENIM ACCUSANTIUM LAUDANTIUM INVENTORE IPSA ISTE SUNT SED SIT IPSAM</div>
  <div class="abs small" style="left:34px;top:44px;color:#777">Sed enim accusantium <span style="color:var(--royal)">laudantium Unde quas</span> quae ratione inventore ipsa iste sunt sed sit ipsam ut voluptatem <span style="color:var(--royal)">doloremque</span></div>
  <div class="abs label">SEE PALVO PERSS</div>
</div>

<div class="abs why-item" style="left:182px;top:1535px"><svg width="22" height="22" viewBox="0 0 22 22"><circle cx="11" cy="11" r="11" fill="#555"/><path d="M7 15l8-8" stroke="#fff" stroke-width="2"/></svg><h4>Ipsa explicabo</h4><p class="small">Dolores ut voluptatem doloremque beatae atione ratione dolores</p></div>
<div class="abs why-item" style="left:397px;top:1535px"><svg width="22" height="22" viewBox="0 0 22 22"><circle cx="11" cy="11" r="11" fill="#555"/><path d="M6 11l4 4 6-8" stroke="#fff" stroke-width="2" fill="none"/></svg><h4>Ratione inventore</h4><p class="small">Dolores ut voluptatem doloremque beatae atione ratione dolores</p></div>
<div class="abs why-item" style="left:610px;top:1535px"><svg width="22" height="22" viewBox="0 0 22 22"><circle cx="11" cy="11" r="11" fill="#555"/><circle cx="11" cy="11" r="5" fill="none" stroke="#fff" stroke-width="2"/></svg><h4>Unde quasi</h4><p class="small">Dolores ut voluptatem doloremque beatae atione ratione dolores</p></div>
<div class="abs why-item" style="left:825px;top:1535px"><svg width="22" height="22" viewBox="0 0 22 22"><circle cx="11" cy="11" r="11" fill="#555"/><rect x="6" y="7" width="10" height="8" fill="#fff"/></svg><h4>Customer support</h4><p class="small">Dolores ut voluptatem doloremque beatae atione ratione dolores</p></div>
<div class="abs why-item" style="left:182px;top:1612px"><svg width="22" height="22" viewBox="0 0 22 22"><circle cx="11" cy="11" r="11" fill="#555"/><ellipse cx="11" cy="10" rx="6" ry="4" fill="#fff"/></svg><h4>Ratione dolores</h4><p class="small">Dolores ut voluptatem doloremque beatae atione ratione dolores</p></div>
<div class="abs why-item" style="left:397px;top:1612px"><svg width="22" height="22" viewBox="0 0 22 22"><circle cx="11" cy="11" r="11" fill="#555"/><rect x="6" y="6" width="10" height="10" fill="none" stroke="#fff" stroke-width="2"/></svg><h4>Beatae quia</h4><p class="small">Dolores ut voluptatem doloremque beatae atione ratione dolores</p></div>
<div class="abs why-item" style="left:610px;top:1612px"><svg width="22" height="22" viewBox="0 0 22 22"><circle cx="11" cy="11" r="11" fill="#555"/><path d="M11 5v6l4 3" stroke="#fff" stroke-width="2" fill="none"/></svg><h4>Beatae atione</h4><p class="small">Dolores ut voluptatem doloremque beatae atione ratione dolores</p></div>
<div class="abs why-item" style="left:825px;top:1612px"><svg width="22" height="22" viewBox="0 0 22 22"><circle cx="11" cy="11" r="11" fill="#555"/><path d="M6 8h10M6 11h10M6 14h10" stroke="#fff" stroke-width="1.5"/></svg><h4>Customer support</h4><p class="small">Dolores ut voluptatem doloremque beatae atione ratione dolores</p></div>

<section class="abs info">
  <div class="abs col-title" style="left:182px;top:58px">Upcoming events</div>
  <div class="abs small" style="left:358px;top:56px;display:flex;align-items:center;gap:12px">view more <span class="dot dark" style="width:18px;height:18px"><svg width="8" height="8" viewBox="0 0 8 8"><path d="M2 1l4 3-4 3z" fill="#fff"/></svg></span></div>
  <div class="abs" style="left:182px;top:86px;width:264px;border-top:1px solid var(--line)"></div>
  <div class="abs date" style="left:182px;top:96px;background:var(--royal)">10<small>Jun</small></div>
  <div class="abs" style="left:226px;top:96px;width:220px">
    <div style="color:var(--royal);font-weight:700;font-size:11px">Veritatis beatae eos aut voluptas</div>
    <div class="small" style="font-size:9px">Doloremque Totam / 9 Comments</div>
    <p class="small" style="margin-top:10px">Enim accusantium laudantium laudantium perspiciatis ipsam sed doloremque totam unde unde, ut aut illo aut</p>
  </div>
  <div class="abs date" style="left:182px;top:200px;background:#aaa">10<small>Jun</small></div>
  <div class="abs" style="left:226px;top:200px;width:220px">
    <div style="color:#555;font-weight:700;font-size:11px">Perspiciatis error natus qui aut eaque</div>
    <div class="small" style="font-size:9px">Doloremque Totam / 9 Comments</div>
    <p class="small" style="margin-top:10px">dolores totam unde ut aut illo aut veritatis explicabo dicta quo veritatis</p>
  </div>

  <div class="abs col-title" style="left:486px;top:58px">Inspector news</div>
  <div class="abs" style="left:486px;top:86px;width:228px;border-top:1px solid var(--line)"></div>
  <div class="abs news-row" style="left:486px;top:96px"><span class="sq" style="background:var(--royal);color:#fff">−</span><b style="color:#555">Doloremque perspiciatis error</b></div>
  <p class="abs small" style="left:486px;top:134px;width:228px">Enim accusantium laudantium laudantium perspiciatis ipsam sed doloremque totam unde unde, ut aut illo aut</p>
  <div class="abs news-row" style="left:486px;top:196px;color:var(--royal)"><span class="sq">+</span>Fugit aut illo omnis explicabo ipsa</div>
  <div class="abs news-row" style="left:486px;top:232px;color:#555"><span class="sq">+</span>Rem ipsam quas illo dolores</div>
  <div class="abs news-row" style="left:486px;top:268px;color:#555"><span class="sq">+</span>Voluptatem doloremque perspiciatis</div>

  <div class="abs col-title" style="left:762px;top:58px">Our testimonilas</div>
  <div class="abs" style="left:762px;top:86px;width:256px;border-top:1px solid var(--line)"></div>
  <div class="abs" style="left:908px;top:204px;text-align:right;font-size:10px"><b style="color:var(--royal)">Mark Orwin</b><br>Project Manager</div>
  <div class="abs" style="left:976px;top:198px;width:42px;height:42px;background:linear-gradient(135deg,#b89c88,#e4d8cf)" role="img" aria-label="Portrait photo of the reviewer"></div>
</section>
<div class="abs quote">" Voluptatem fugit aut illo omnis explicabo ipsa nemo rem ipsam quas illo dolores ut voluptatem doloremque perspiciatis beatae magni architecto odit odit</div>
<svg class="abs" style="left:980px;top:1892px" width="22" height="14" viewBox="0 0 22 14"><path d="M0 0h22L22 14z" fill="#444"/></svg>

<section class="abs partners">
  <div class="abs heading" style="left:182px;top:60px">Best partner</div>
</section>
<div class="abs partner" style="left:182px">HALDEN</div>
<div class="abs partner" style="left:404px">ARVO</div>
<div class="abs partner" style="left:552px">Corvin</div>
<div class="abs partner" style="left:728px">cityvale</div>
<div class="abs partner" style="left:890px">TOONWAY</div>

<footer class="abs footer">
  <div class="abs" style="left:178px;top:56px;width:200px">
    <h5>Who we are</h5>
    <p class="txt" style="margin-top:14px">Fugit aut illo omnis explicabo ipsa, nemo ipsam quasi dolores voluptatem dolo perspiciatis beatae magni architecto odit</p>
    <div class="txt" style="margin-top:22px;color:#fff;display:flex;align-items:center;gap:8px">Read More <span class="dot" style="width:14px;height:14px"></span></div>
  </div>
  <div class="abs" style="left:398px;top:56px;width:180px">
    <h5>Adreess</h5>
    <p class="txt" style="margin-top:14px">2400 Linden Way Suite 12<br>Fairhaven CA 95000-0100<br>Hours M-F 8:00am-5:00pm<br>Fax: 916 555 0163</p>
    <div class="txt" style="margin-top:22px;display:flex;align-items:center;gap:10px"><svg width="12" height="16" viewBox="0 0 12 16"><path d="M6 0a6 6 0 0 1 6 6c0 4-6 10-6 10S0 10 0 6a6 6 0 0 1 6-6z" fill="#fff"/><circle cx="6" cy="6" r="2" fill="#3b3b3b"/></svg>Open in Map</div>
  </div>
  <div class="abs" style="left:574px;top:56px;width:170px">
    <h5>PALVO Perss <span class="dot" style="width:14px;height:14px;margin-left:60px"></span></h5>
    <div style="margin-top:14px;display:grid;grid-template-columns:72px 72px;gap:10px 16px">
      <div class="thumb" role="img" aria-label="News photo"></div><div class="thumb" role="img" aria-label="News photo"></div>
      <div class="thumb" role="img" aria-label="News photo"></div><div class="thumb" role="img" aria-label="News photo"></div>
    </div>
  </div>
  <div class="abs" style="left:782px;top:56px;width:236px">
    <h5>Tweets <span class="dot" style="width:14px;height:14px;margin-left:164px"></span></h5>
    <div class="tweet" style="margin-top:14px"><svg width="14" height="12" viewBox="0 0 14 12"><rect width="14" height="12" rx="3" fill="#888"/></svg><span style="flex:1">@ ratione inventore ipsa<br>ecsyfhtfhs</span><span style="color:#fff;text-align:center">2<br><small>days ago</small></span></div>
    <div class="tweet" style="margin-top:8px"><svg width="14" height="12" viewBox="0 0 14 12"><rect width="14" height="12" rx="3" fill="#888"/></svg><span style="flex:1">@ ratione inventore ipsa<br>ecsyfhtfhs</span><span style="color:#fff;text-align:center">2<br><small>days ago</small></span></div>
  </div>
</footer>

<div class="abs bottombar">
  <div class="abs" style="left:178px;top:38px">© 2013 PALVO. All Rights Reserved.</div>
  <div class="abs" style="left:421px;top:38px;display:flex;gap:24px"><span>about us</span><span>lates news</span><span>popular</span><span>privacy policy</span><span>FAQs</span><span>contact us</span></div>
</div>

</body>
</html>
```